Concept design for a tea business Labels

Hello, we are looking for concepts for our label/packaging for a tea business that has been in business now for over a year. We are a beachy, organic, "It's your moment. Enjoy it." type tea business. We have an online website (www.corvalbrewhouse.com.au) and sell at local markets around the Tarrowby Cove area.
We are looking to upgrade our label to look more professional, in a fun/beachy/chilled out style. (unlike the traditional tea labels).
We do loose leaf tea and iced tea consentrated syrups. We have a few different packages (please see website under "sizes and packaging" bottom left). We would like to experiement with various different size and shape of labels for different products, so would like a concept design for a label using our logo (see website front page bottom). There are no colour constraints.
We use the Quillan brand labels of the following sizes:
1. Pure Glass Rectangular Product Labels, Q4825, 100/Pack, 96 x 50.8 mm
2. Pure Glass Round Multi-purpose Labels, Q3907D, 240/Pack, 40 mm diameter
3.Pure Glass Square Product Labels, Q4861, 350/Pack, 35 x 35 mm
4. For bottles we use Grained Ivory Curved Labels, Q4839, 90/Pack, 57.2 x 77 mm
If you have any more questions, please don't hesitate to contact me
Updates
Hi All,
I am considering using a box like below for packing and doing a bit of a white/beachy feel to the packaging. Either using the rectangle or round circle labels. (circle labels from quillan 60mm diameter).

Reason: Hi All - Thank you so much for all your designs. While I have seen some really beautiful designs I am excited about, it seems there was a rush at the end with a number of new designs just submitted. I still haven't seen just one design I love for the label, so I would like the opportunity to work with some of the new designers to see if we can modify to suit the concept.
Would anyone like to try a concept label with a silhouette of one of the following wave/beach/teacup? I'm just exploring a different approach as I know it is difficult tying in the beach with tea - please think - chilled out beach hut with tea/iced tea, sunrise over ocean. I like the soft colour palette - beachy feel to it - ie. Pastels - blues, greens, whites, sandy, pinks, purples, greys - sunrises over ocean, maybe a white rustic wood feel - or any other icon from Tarrowby Cove - like the Norfolk Pine's along the beach - maybe in Silhouette.
Just some more ideas.
Thank you again for all your contributions!
Petra

```html
<!DOCTYPE html>
<html lang="en">
<head>
<meta charset="utf-8">
<title>Tarrowby Tea Company – Packaging Concept</title>
<link href="https://fonts.googleapis.com/css2?family=Cinzel:wght@700&family=Lato:wght@400;700&display=swap" rel="stylesheet">
<style>
  :root {
    --canvas: #ffffff;
    --seafoam: #5cc6b8;
    --seafoam-deep: #3fae9f;
    --seafoam-faint: #d6efeb;
    --lid-grey: #c8cacc;
    --lid-grey-dark: #b2b5b7;
    --label-white: #ffffff;
    --accent-red: #e0504a;
    --ink-soft: #6f7d7b;
  }
  * { margin: 0; padding: 0; box-sizing: border-box; }
  html, body { width: 1200px; height: 695px; overflow: hidden; background: var(--canvas); }
  body { font-family: "Lato", sans-serif; }

  .canvas { position: relative; width: 1200px; height: 695px; background: var(--canvas); }

  /* faint brand seal in the background */
  .brand-seal {
    position: absolute; left: 60px; top: 20px;
    width: 470px; height: 470px; border-radius: 50%;
    border: 14px solid var(--seafoam-faint);
    display: flex; align-items: center; justify-content: center;
  }
  .brand-seal__name {
    font-family: "Cinzel", serif; font-weight: 700;
    font-size: 40px; color: var(--seafoam-faint);
    text-align: center; line-height: 1.2; letter-spacing: 2px;
  }

  /* flat box fronts */
  .box {
    position: absolute; width: 300px; height: 300px;
    display: flex; flex-direction: column;
    box-shadow: 0 0 0 1px #e3e6e6;
  }
  .box--plain { left: 230px; top: 330px; }
  .box--named { left: 620px; top: 300px; }

  .box__lid {
    height: 52%; background: linear-gradient(180deg, var(--lid-grey) 0%, var(--lid-grey-dark) 100%);
    position: relative;
  }
  .box__base {
    flex: 1; position: relative;
    background: linear-gradient(180deg, var(--seafoam) 0%, var(--seafoam-deep) 100%);
  }

  .round-label {
    position: absolute; width: 112px; height: 112px; border-radius: 50%;
    background: var(--label-white);
    display: flex; align-items: center; justify-content: center;
  }
  .round-label__core {
    width: 94px; height: 94px; border-radius: 50%;
    background: var(--seafoam);
    display: flex; align-items: center; justify-content: center;
    text-align: center;
    font-family: "Lato", sans-serif; font-weight: 700;
    font-size: 12px; line-height: 1.25; color: var(--label-white);
  }
  .box--plain .round-label { left: 94px; top: 48px; }
  .box--named .round-label { left: 94px; top: 90px; }

  .box__flavour {
    position: absolute; left: 0; right: 0; top: 40px;
    text-align: center; font-size: 18px; font-weight: 700;
    color: var(--accent-red); letter-spacing: 0.5px;
  }
  .box__details {
    position: absolute; left: 0; right: 0; bottom: 16px;
    text-align: center; font-size: 11px; color: var(--label-white);
    letter-spacing: 1px; text-transform: uppercase;
  }
</style>
</head>
<body>
<main class="canvas">
  <div class="brand-seal" aria-hidden="true">
    <p class="brand-seal__name">Tarrowby<br>Tea Company</p>
  </div>

  <section class="box box--plain" aria-label="Box front, plain lid">
    <div class="box__lid">
      <div class="round-label"><div class="round-label__core">Tarrowby<br>Tea<br>Company</div></div>
    </div>
    <div class="box__base" role="img" aria-label="Soft seafoam striped band pattern">
      <p class="box__details">Loose Leaf Tea · Net 50g</p>
    </div>
  </section>

  <section class="box box--named" aria-label="Box front, flavour lid">
    <div class="box__lid">
      <p class="box__flavour">Chamomile Blend</p>
    </div>
    <div class="box__base" role="img" aria-label="Soft seafoam striped band pattern"></div>
    <div class="round-label"><div class="round-label__core">Tarrowby<br>Tea<br>Company</div></div>
  </section>
</main>
</body>
</html>
```